Employee Benefits Consulting Firm needs a refreshed website

I have a business (an employee benefits consulting firm) called KRV Benefits Group, LLC (www.krvbenefits-example.com).  The existing site is currently hosted on Nimbuspark.  The business has been pretty much dormant since 2012.  I've relaunched the business and need a new website and looking for the website to be in Wordpress and to start with just 5 pages:
Home
About Us
Services
Contact Us
Blog
Some information about KRV Benefits Group:
There is a tremendous waste (financial) in the traditional employee benefit model --- the current system is broken and simply stated, unsustainable. We take a very different approach when it comes to employee benefits consulting, constantly strive to provide short-term and long-term cost containment strategies that truly bend the healthcare cost curve... Many of our clients consider us as Benefit Architects...
Each employer/business is unique.
In short, our firm works with Employers to first understand their business.... -their history, their corporate structure, their leadership, their values, their uniqueness, etc.
Then we take a deep dive and get a strong grasp on their existing benefits program... -how did they get to where they are today, what are their goals/objectives, what is their risk tolerance, what are current pain points, are they compliant, etc.
Then after thorough analysis, we deliver a tailored solution. We implement the programs and manage the various aspects and moving parts of the program throughout the year.
We also are constantly analyzing the performance of the plan and monitor population health. We aggregate data and constantly refine the approach/strategy.

Updates
I made a few updates to the brief over the past couple of days...below is the updated brief:
Home
About Us
Services
Contact Us
Blog
MUST HAVE:
Mobile Friendly
PLEASE USE TORVEL THEME
SHOULD HAVE:
the ability to add embedded video client testimonials
the ability for online chat
SHOULD NOT HAVE:
Photos from the old/existing website, I apologize for the late directive

I apologize for the delay on responding. Content is just about complete and will submit ASAP. Please let me know your availability to complete this project.

Updated content has been posted to this project.  I appreciate everybody's patience as we are working through this!

Target Market(s)
This is a BtoB website, primarily focusing on the following targets: CFOs, CEOs, Directors of Human Resources
Industry/Entity Type
Consulting
Number of Pages Required
5+ page
Requirements
Must have
- Mobile Friendly
- PLEASE USE TORVEL THEME
Nice to have
- the ability to add embedded video client testimonials
- the ability for online chat
Should not have
- Photos from the old/existing website, I apologise for the late directive

```html
<!DOCTYPE html>
<html lang="en">
<head>
<meta charset="utf-8">
<title>KRV Benefits Group — Home</title>
<link rel="stylesheet" href="https://fonts.googleapis.com/css2?family=Poppins:wght@400;500;600;700&family=Open+Sans:ital,wght@0,400;0,600;0,700;1,400&family=Montserrat:wght@300;400;700&display=swap">
<style>
:root{
  --navy:#3f5568;
  --navy-deep:#3a4c5e;
  --slate:#4a5b6d;
  --slate-light:#8e9aa7;
  --green:#5aab47;
  --mint:#a8ddd5;
  --ink:#333;
  --muted:#666;
  --footer:#222;
  --footer-bottom:#1a1a1a;
  --white:#fff;
}
*{margin:0;padding:0;box-sizing:border-box}
html,body{width:1200px;height:1200px;overflow:hidden;background:var(--white)}
.stage{position:absolute;left:0;top:0;width:1932px;height:1932px;transform:scale(.62112);transform-origin:0 0}
.page{position:absolute;left:622px;top:0;width:688px;height:1932px;background:var(--white);font-family:"Open Sans",sans-serif;color:var(--ink);overflow:hidden}
.abs{position:absolute}
.heading{font-family:"Poppins",sans-serif;font-weight:700;color:var(--navy);letter-spacing:-.3px}
.btn{position:absolute;background:var(--green);color:var(--white);font-family:"Montserrat",sans-serif;font-weight:700;font-size:3.6px;display:flex;align-items:center;justify-content:center;letter-spacing:.2px}
.photo{position:absolute}

/* top bar + header */
.topbar{left:0;top:0;width:688px;height:11px;background:var(--navy);color:#dfe6ec;font-size:4.3px;line-height:5px}
.topbar span{position:absolute;top:0}
.header{left:0;top:11px;width:688px;height:38px;background:var(--white)}
.brand{left:88px;top:12px;display:flex;align-items:center;gap:4px;font-family:"Poppins",sans-serif;font-weight:500;font-size:10px;color:var(--navy)}
.brand i{width:9px;height:9px;border-radius:50%;background:var(--green);display:block}
.nav a{position:absolute;top:13px;font-family:"Montserrat",sans-serif;font-weight:700;font-size:4.5px;color:var(--navy);text-decoration:none;line-height:13px}
.nav a.active{background:var(--green);color:var(--white);width:36px;text-align:center}

/* hero */
.hero{left:0;top:49px;width:688px;height:290px;background:linear-gradient(100deg,#5d6d7e 0%,#6f7f8f 40%,#8c9aa8 70%,#a8b2bb 100%)}
.hero-title{left:133px;top:145px;font-size:21px;line-height:24.5px;color:var(--white);letter-spacing:-.8px}
.hero-text{left:134px;top:200px;width:195px;font-size:5.6px;line-height:9px;color:#eef2f5}
.arrow{position:absolute;width:12px;height:12px;border-radius:50%;background:rgba(255,255,255,.35);display:flex;align-items:center;justify-content:center}
.steps{left:84px;top:300px;width:516px;height:84px;display:flex}
.step{width:129px;height:84px;display:flex;align-items:center;padding-left:58px;font-family:"Poppins",sans-serif;font-weight:700;font-size:7px;line-height:9.5px;color:var(--white);text-transform:uppercase}
.step.dark{background:var(--slate)}
.step.light{background:var(--slate-light)}
.step.center{padding-left:0;justify-content:center;padding-left:20px}
.step.wide{padding-left:74px}

/* services */
.label{font-size:3.8px;color:#999;letter-spacing:.3px}
.body-text{font-size:5.4px;line-height:10.7px;color:var(--muted)}
.link{font-size:5.4px;color:var(--green);text-decoration:underline;font-weight:600}
.svc{position:absolute;width:100px;text-align:center}
.svc h3{font-family:"Poppins",sans-serif;font-weight:400;font-size:6.8px;color:var(--ink);margin-top:0}
.svc p{font-size:5.2px;line-height:9px;color:var(--ink);margin-top:5px}
.svc .link{display:block;margin-top:6px}

/* commitment */
.commit-title{left:0;width:688px;top:630px;text-align:center;font-family:"Poppins",sans-serif;font-weight:700;font-size:12px;color:var(--white)}
.commit-text{left:0;width:688px;top:653px;text-align:center;font-family:"Montserrat",sans-serif;font-weight:300;font-size:12.6px;line-height:18px;color:var(--white)}

/* team */
.section-title{left:0;width:688px;text-align:center;font-size:12px}
.member{position:absolute;top:826px;width:133px;text-align:center}
.member .portrait{width:133px;height:139px;background:linear-gradient(180deg,#cfd6dc,#9aa7b3)}
.member h4{font-family:"Poppins",sans-serif;font-weight:700;font-size:7.6px;color:var(--navy);margin-top:9px}
.member p{font-size:3.8px;color:var(--green);margin-top:1px}

/* testimonial */
.testimonial{left:0;top:1033px;width:688px;height:181px;background:var(--mint)}
.quote{left:0;width:688px;top:1118px;text-align:center;font-style:italic;font-size:6.2px;line-height:13px;color:var(--navy)}
.diamond{position:absolute;width:13px;height:13px;transform:rotate(45deg)}
.dot{position:absolute;width:4px;height:4px;border-radius:50%;background:#eaf7f4}

/* newsletter */
.newsletter{left:0;top:1214px;width:688px;height:74px;background:var(--navy)}
.field{position:absolute;background:var(--white);font-size:4px;color:#777;padding-left:9px;display:flex;align-items:center}

/* blog */
.post{position:absolute;top:1359px;width:133px;text-align:center}
.post .thumb{width:133px;height:87px}
.post h4{font-family:"Poppins",sans-serif;font-weight:600;font-size:6.4px;color:var(--ink);margin-top:9px}
.post .date{font-size:3.6px;color:#999;margin-top:3px}
.post p{font-size:4.5px;line-height:10px;color:var(--muted);margin-top:4px}

/* contact */
.contact{left:0;top:1567px;width:688px;height:200px;background:linear-gradient(135deg,#3a4d60,#43586c)}

/* footer */
.footer{left:0;top:1767px;width:688px;height:148px;background:var(--footer)}
.footer-bottom{left:0;top:1915px;width:688px;height:17px;background:var(--footer-bottom);color:#777;font-size:3.8px;text-align:center;line-height:24px}
.f-head{font-family:"Montserrat",sans-serif;font-weight:700;font-size:4.4px;color:var(--white);text-decoration:underline}
.f-label{font-size:3.5px;color:var(--green);font-weight:700}
.f-text{font-size:4.8px;color:#bbb;line-height:9.3px}
.social{position:absolute;top:1811px;width:4px;height:4px;border-radius:50%;background:var(--white)}
</style>
</head>
<body>
<div class="stage">
<div class="page">

  <!-- top bar -->
  <div class="abs topbar">
    <span style="left:92px">info@krvbenefits-example.com</span>
    <span style="left:186px">(555) 014-2290</span>
    <svg class="abs" style="left:470px;top:0" width="5" height="6" viewBox="0 0 10 12"><path d="M5 0a4 4 0 0 0-4 4c0 3 4 8 4 8s4-5 4-8a4 4 0 0 0-4-4z" fill="#fff"/></svg>
    <span style="left:478px">4870 Alder Crest Blvd, Ste. 210, Dallas, TX 75240</span>
  </div>

  <!-- header -->
  <header class="abs header">
    <div class="abs brand"><i></i>KRV Benefits Group</div>
    <nav class="nav">
      <a class="active" style="left:390px">HOME</a>
      <a style="left:435px">ABOUT US</a>
      <a style="left:476px">SERVICES</a>
      <a style="left:519px">CONTACT US</a>
      <a style="left:569px">BLOG</a>
    </nav>
  </header>

  <!-- hero -->
  <section class="abs hero" role="img" aria-label="Photo of a smiling consulting team at work in a bright office"></section>
  <h1 class="abs heading hero-title" style="color:#fff">The key to benefits<br>is to be competitive</h1>
  <p class="abs hero-text">At KRV Benefits Group we know your company gains competitive advantages from an experienced and hard working team.</p>
  <div class="btn" style="left:134px;top:229px;width:59px;height:14px">CONTACT US</div>
  <div class="arrow" style="left:63px;top:171px"><svg width="5" height="5" viewBox="0 0 10 10"><path d="M7 1L3 5l4 4" stroke="#fff" stroke-width="1.6" fill="none"/></svg></div>
  <div class="arrow" style="left:612px;top:171px"><svg width="5" height="5" viewBox="0 0 10 10"><path d="M3 1l4 4-4 4" stroke="#fff" stroke-width="1.6" fill="none"/></svg></div>
  <svg class="abs" style="left:0;top:270px" width="688" height="80" viewBox="0 0 688 80">
    <path d="M0 10 Q344 150 688 10 V80 H0 Z" fill="#5aab47"/>
    <path d="M0 24 Q344 168 688 24 V80 H0 Z" fill="#fff"/>
  </svg>
  <div class="abs steps">
    <div class="step dark">Plan<br>&amp; Analyze</div>
    <div class="step light">Design<br>&amp; Build</div>
    <div class="step dark" style="padding-left:74px">Implement</div>
    <div class="step light">Managed<br>Year<br>Round</div>
  </div>

  <!-- services -->
  <p class="abs label" style="left:145px;top:431px">OUR SERVICES</p>
  <h2 class="abs heading" style="left:145px;top:438px;font-size:12px">What We Do For You</h2>
  <p class="abs body-text" style="left:145px;top:458px;width:132px">Saving money on employee benefits while still attracting and retaining the best and the brightest is a must in today's economy. The cost of providing benefits is rising significantly, while employees consistently seek more and more from their benefits packages.</p>
  <span class="abs link" style="left:145px;top:527px">More Services</span>

  <svg class="abs" style="left:354px;top:430px" width="34" height="34" viewBox="0 0 34 34" fill="none" stroke="#3f5568" stroke-width="1.2">
    <rect x="7" y="6" width="20" height="16" rx="2"/><circle cx="17" cy="6" r="3.5" fill="#5aab47" stroke="none"/><path d="M3 28h10l6-4h8M3 31h24"/>
  </svg>
  <div class="svc" style="left:321px;top:474px">
    <h3>The KRV Benefits</h3>
    <p>Your employees are your most valuable assets. Helping them stay healthy and productive not only benefits workers and their families</p>
    <span class="link">Read More</span>
  </div>
  <svg class="abs" style="left:483px;top:430px" width="34" height="34" viewBox="0 0 34 34" fill="none" stroke="#3f5568" stroke-width="1.2">
    <circle cx="17" cy="10" r="5" fill="#5aab47" stroke="none"/><path d="M4 32V14M30 32V14M10 32V20h14v12M13 24v8M17 24v8M21 24v8"/>
  </svg>
  <div class="svc" style="left:449px;top:474px">
    <h3>KRV Assurance</h3>
    <p>Whether you want to make sure the mortgage will get paid, your children will go to college</p>
    <span class="link" style="margin-top:15px">Read More</span>
  </div>

  <!-- commitment -->
  <svg class="abs" style="left:0;top:571px" width="688" height="180" viewBox="0 0 688 180" role="img" aria-label="Faded photo of an office desk with a laptop">
    <defs><linearGradient id="commitFill" x1="0" x2="1"><stop offset="0" stop-color="#8a98a8"/><stop offset=".5" stop-color="#9aa6b3"/><stop offset="1" stop-color="#8d9bab"/></linearGradient></defs>
    <path d="M0 32 Q344 -32 688 32 L688 142 Q344 216 0 142 Z" fill="url(#commitFill)"/>
  </svg>
  <h2 class="abs commit-title">COMMITMENT</h2>
  <p class="abs commit-text">Our goal is long-term relationships<br>and we realize that these are earned</p>

  <!-- team -->
  <h2 class="abs heading section-title" style="top:795px">Meet Our Teams</h2>
  <div class="member" style="left:134px"><div class="portrait" role="img" aria-label="Portrait of the firm's president"></div><h4>Daniel Hartwell CBC</h4><p>President</p></div>
  <div class="member" style="left:278px"><div class="portrait" role="img" aria-label="Portrait of an employee benefit consultant" style="background:linear-gradient(180deg,#b9c6d2,#6e88a6)"></div><h4>Marcus Ellery CBC</h4><p>Employee Benefit Consultant</p></div>
  <div class="member" style="left:421px"><div class="portrait" role="img" aria-label="Portrait of an employee benefits consultant" style="background:linear-gradient(180deg,#9fb0bf,#5b6570)"></div><h4>Claire Whitmore</h4><p>Employee Benefits Consultant</p></div>
  <div class="arrow" style="left:103px;top:891px;background:#eee"><svg width="5" height="5" viewBox="0 0 10 10"><path d="M7 1L3 5l4 4" stroke="#bbb" stroke-width="1.6" fill="none"/></svg></div>
  <div class="arrow" style="left:569px;top:891px;background:var(--navy)"><svg width="5" height="5" viewBox="0 0 10 10"><path d="M3 1l4 4-4 4" stroke="#fff" stroke-width="1.6" fill="none"/></svg></div>

  <!-- testimonial -->
  <section class="abs testimonial"></section>
  <div class="abs" style="left:280px;top:1083px;width:20px;height:20px;border-radius:50%;background:#fff"></div>
  <p class="abs" style="left:313px;top:1089px;font-size:4.6px;font-weight:700;color:var(--ink)">Nora Fielding - <span style="color:#fff;font-weight:600">HR Manager / City of Brantley</span></p>
  <p class="abs quote">" KRV was able to save the City enough money on our current insurance that we were able to<br>provide our employees with an additional benefit of Long Term Disability."</p>
  <div class="diamond" style="left:139px;top:1118px;background:#fff"></div>
  <div class="diamond" style="left:537px;top:1118px;background:var(--navy)"></div>
  <div class="dot" style="left:331px;top:1157px"></div>
  <div class="dot" style="left:346px;top:1157px;background:var(--green)"></div>
  <div class="dot" style="left:361px;top:1157px"></div>

  <!-- newsletter -->
  <section class="abs newsletter"></section>
  <h3 class="abs heading" style="left:136px;top:1240px;font-size:10px;color:#fff">Email Newsletters</h3>
  <p class="abs" style="left:136px;top:1255px;font-size:4.3px;color:#dfe6ec">Keep me up to date with content, updates, and offers from Rowan</p>
  <div class="field" style="left:340px;top:1247px;width:146px;height:15px">Email address</div>
  <div class="btn" style="left:486px;top:1247px;width:66px;height:15px">SUBSCRIBE</div>

  <!-- blog -->
  <p class="abs label" style="left:0;width:688px;text-align:center;top:1323px">LATEST NEWS</p>
  <h2 class="abs heading section-title" style="top:1329px;color:#222">From Blog News</h2>
  <article class="post" style="left:134px"><div class="thumb" role="img" aria-label="Photo of coworkers at desks in an open office" style="background:linear-gradient(135deg,#b7a184,#6d665e)"></div><h4>velit aliquetpraesent commodo</h4><p class="date">February 3, 2019</p><p>Integer posuere erat a ante venenatis dapibus posuere velit aliquetpraesent commodo cursus magna.</p></article>
  <article class="post" style="left:278px"><div class="thumb" role="img" aria-label="Photo of a team meeting under a hanging bulb" style="background:linear-gradient(135deg,#8a5a45,#3d3431)"></div><h4>velit aliquetpraesent commodo</h4><p class="date">February 3, 2019</p><p>Integer posuere erat a ante venenatis dapibus posuere velit aliquetpraesent commodo cursus magna.</p></article>
  <article class="post" style="left:421px"><div class="thumb" role="img" aria-label="Photo of a smiling business team standing together" style="background:linear-gradient(135deg,#8e9399,#3f454c)"></div><h4>velit aliquetpraesent commod</h4><p class="date">February 3, 2019</p><p>Integer posuere erat a ante venenatis dapibus posuere velit aliquetpraesent commodo cursus magna.</p></article>
  <div class="btn" style="left:163px;top:1508px;width:59px;height:14px">READ MORE</div>
  <div class="btn" style="left:310px;top:1508px;width:59px;height:14px">READ MORE</div>
  <div class="btn" style="left:454px;top:1508px;width:59px;height:14px">READ MORE</div>

  <!-- contact -->
  <section class="abs contact"></section>
  <h2 class="abs heading section-title" style="top:1598px;color:#fff;left:3px">Contact Us</h2>
  <div class="field" style="left:136px;top:1626px;width:135px;height:17px">Name</div>
  <div class="field" style="left:279px;top:1626px;width:135px;height:17px">Email</div>
  <div class="field" style="left:422px;top:1626px;width:135px;height:17px">Subject</div>
  <div class="field" style="left:136px;top:1651px;width:421px;height:53px;align-items:flex-start;padding-top:5px">Message</div>
  <div class="btn" style="left:283px;top:1717px;width:126px;height:17px">SUBMIT NOW</div>

  <!-- footer -->
  <footer class="abs footer"></footer>
  <div class="abs brand" style="left:136px;top:1797px;font-size:8px;color:#fff"><i style="width:7px;height:7px"></i>KRV Benefits Group</div>
  <p class="abs f-text" style="left:134px;top:1827px;width:100px">Our innovative team approach blends your unique needs with our creative thinking, comprehensive expertise, and in-depth resources to help you and your employees with benefit management, plan design, and employee communication.</p>
  <p class="abs f-head" style="left:274px;top:1790px">CONTACT US</p>
  <p class="abs f-label" style="left:274px;top:1809px">BUSINESS ADDRESS</p>
  <p class="abs f-text" style="left:274px;top:1816px">Dallas Office Location<br>4870 Alder Crest Blvd, Ste. 210<br>Dallas, TX 75240</p>
  <p class="abs f-label" style="left:274px;top:1851px">BUSINESS PHONE</p>
  <p class="abs f-text" style="left:274px;top:1857px">Main Number: (555) 014-2290</p>
  <p class="abs f-label" style="left:274px;top:1874px">BUSINESS EMAIL</p>
  <p class="abs f-text" style="left:274px;top:1880px">info@krvbenefits-example.com</p>
  <p class="abs f-head" style="left:397px;top:1790px">MENU</p>
  <p class="abs f-text" style="left:397px;top:1807px;line-height:15px">Home<br>About Us<br>Services<br>Contact Us<br>Blogs</p>
  <p class="abs f-text" style="left:446px;top:1807px;line-height:15px">Terms of Use<br>Privacy Policy</p>
  <span class="social" style="left:526px"></span>
  <span class="social" style="left:537px"></span>
  <span class="social" style="left:548px"></span>
  <div class="abs footer-bottom">Copyright 2019 All Rights Reserved. KRV Benefits Group, LLC</div>

</div>
</div>
</body>
</html>
```